2013 Golf Outing Flyer

Our charitable organization was created in honor of my daughter who died at age 16. Our annual fundraiser is a golf tournament. I am not a creative person so I'd like someone to design a printable flyer that grabs people's attention but is not too busy while incorportating our organization's logo with the basic information.

Event details:
3rd Annual Marissa Joan Caldwell Memorial Golf Tournament
4 person scramble

Saturday October 5th, 2013
Larkspur Golf Club, Auburn, IL
9:30 Registration
Shotgun start at noon
To Register go online to www.marissajcaldwellgolf.teesignups.example or email
marissacaldwellfund@mailbox.example

Scholarships to Cedar Rapids Hollow High School seniors are made possible by our orgnization through this fundraiser.
Updates

Target Market(s)

golfers and businesses willing to sponsor event

Industry/Entity Type

School

Requirements
Must have
• single page-easy to print
includes non profit organization logo which I attached (think I did)
Specific information about the tournament- date and location and registration info
Nice to have
• company logo and the golf outing logo but if both are too much, then just the golf logo and the organization name can be at the bottom

```html
<!DOCTYPE html>
<html lang="en">
<head>
<meta charset="utf-8">
<title>3rd Annual Marissa Joan Caldwell Memorial Golf Tournament</title>
<link rel="stylesheet" href="https://fonts.googleapis.com/css2?family=Open+Sans:wght@400;600;700;800&display=swap">
<style>
  :root {
    --ink-white: #ffffff;
    --headline-outline: #3a3320;
    --alert-red: #e8231f;
    --link-red: #e5352c;
    --accent-orange: #f0a020;
    --panel-black: rgba(18, 18, 18, 0.9);
    --field-deep: #2f5a2a;
    --field-mid: #6f9a3e;
    --sky-haze: #8fb3a6;
    --sky-top: #a39868;
    --band-sky: #6f9ed8;
    --band-sky-light: #cfe0f2;
    --band-grass: #4f8a2c;
    --cause-red: #d7282f;
  }
  * { box-sizing: border-box; margin: 0; padding: 0; }
  html, body { width: 848px; height: 1200px; overflow: hidden; background: #ffffff; }
  body { font-family: "Open Sans", Arial, sans-serif; }

  .flyer { position: relative; width: 848px; height: 1200px; overflow: hidden; }

  .course-photo {
    position: absolute; inset: 0 0 180px 0;
    background:
      radial-gradient(ellipse 420px 560px at 690px 560px, rgba(20, 20, 16, 0.75), rgba(20, 20, 16, 0) 70%),
      linear-gradient(180deg, var(--sky-top) 0%, var(--sky-haze) 22%, var(--field-mid) 48%, var(--field-deep) 70%, #1f3a1c 100%);
  }

  .headline { position: absolute; left: 30px; top: 10px; color: var(--ink-white); }
  .headline-annual {
    font-size: 92px; font-weight: 800; line-height: 1; letter-spacing: 1px;
    text-shadow: 0 0 3px var(--headline-outline), 2px 2px 0 var(--headline-outline), -2px -2px 0 var(--headline-outline), 2px -2px 0 var(--headline-outline), -2px 2px 0 var(--headline-outline);
  }
  .headline-annual sup { font-size: 48px; vertical-align: 38px; }
  .headline-title {
    margin-top: 10px; font-size: 33px; font-weight: 800; line-height: 1.08;
    text-transform: uppercase;
    text-shadow: 1px 1px 0 var(--headline-outline), -1px -1px 0 var(--headline-outline), 1px -1px 0 var(--headline-outline), -1px 1px 0 var(--headline-outline);
  }
  .headline-format {
    margin-top: 6px; font-size: 33px; font-weight: 800; color: var(--alert-red);
    text-shadow: 1px 1px 0 #fff, -1px -1px 0 #fff, 1px -1px 0 #fff, -1px 1px 0 #fff;
  }

  .details-panel {
    position: absolute; left: 37px; top: 290px; width: 478px; height: 480px;
    background: var(--panel-black); padding: 52px 0 0 31px; color: var(--ink-white);
  }
  .details-list { list-style: none; }
  .details-list li { font-size: 24px; line-height: 52px; text-transform: uppercase; letter-spacing: 0.5px; }
  .details-list .detail-start { color: var(--accent-orange); }
  .register { margin-top: 30px; font-size: 19px; line-height: 30px; }
  .register a { color: var(--link-red); text-decoration: none; display: block; }
  .register-alt { margin-top: 30px; }

  .scholarship { position: absolute; left: 42px; top: 828px; color: var(--ink-white); }
  .scholarship-word { font-size: 76px; font-weight: 400; line-height: 1; letter-spacing: -0.5px; }
  .scholarship-recipients { font-size: 24px; font-weight: 700; color: var(--accent-orange); margin-top: 2px; }
  .scholarship-note { font-size: 20px; margin-top: 2px; }

  .cause-band {
    position: absolute; left: 0; bottom: 0; width: 848px; height: 180px;
    background: linear-gradient(180deg, var(--band-sky) 0%, var(--band-sky-light) 100%);
  }
  .tee-photo {
    position: absolute; right: 0; bottom: 0; width: 300px; height: 180px;
    background:
      radial-gradient(circle 42px at 142px 62px, #ffffff 0 95%, rgba(255,255,255,0) 100%),
      linear-gradient(180deg, rgba(0,0,0,0) 60%, var(--band-grass) 80%);
  }
  .cause-mark { position: absolute; left: 20px; top: 48px; display: flex; align-items: center; gap: 14px; }
  .cause-square { width: 22px; height: 22px; background: var(--cause-red); }
  .cause-name {
    color: var(--cause-red); font-weight: 800; font-size: 40px; line-height: 1.05;
    text-transform: uppercase; letter-spacing: 2px;
  }
  .cause-name span { display: block; font-size: 22px; letter-spacing: 1px; }
</style>
</head>
<body>
<main class="flyer">
  <div class="course-photo" role="img" aria-label="Golf bag full of clubs standing on a softly blurred green fairway"></div>

  <header class="headline">
    <h1 class="headline-annual">3<sup>RD</sup> ANNUAL</h1>
    <p class="headline-title">Marissa Joan Caldwell Memorial<br>Golf Tournament</p>
    <p class="headline-format">4 PERSON SCRAMBLE</p>
  </header>

  <section class="details-panel">
    <ul class="details-list">
      <li>Saturday October 5th, 2013</li>
      <li>Larkspur Golf Club, Auburn, IL</li>
      <li>9:30 Registration</li>
      <li class="detail-start">Shotgun start at noon</li>
    </ul>
    <p class="register">To Register go online to
      <a href="#">www.marissajcaldwellgolf.teesignups.example</a></p>
    <p class="register register-alt">or email
      <a href="#">marissacaldwellfund@mailbox.example</a></p>
  </section>

  <section class="scholarship">
    <p class="scholarship-word">Scholarships</p>
    <p class="scholarship-recipients">to Cedar Rapids Hollow High School seniors</p>
    <p class="scholarship-note">are made possible by our orgnization through this fundraiser.</p>
  </section>

  <footer class="cause-band">
    <div class="tee-photo" role="img" aria-label="Golf ball on a tee in grass under a blue sky"></div>
    <div class="cause-mark">
      <div class="cause-square"></div>
      <p class="cause-name">Golf Tournament<span>Golfing for a cause</span></p>
    </div>
  </footer>
</main>
</body>
</html>
```